Creative Flyer Design Project

I want to create a flyer. I have attached wireframe (wireframe.png) of flyer which gives you much needed idea regarding flyer content. I have attached few images from our portfolio which can be used while designing a flyer.

I would like you to show me the extreme creativity and capability in delivering world class flyer design.

No heavy graphics needed. I want extremely clean and professional flyer using icons, colors and highlighted text/headings.

I will be requiring multiple formats of flyer such as .ai/.png/.psd/pdf.

Size of flyer: Standard A4 size OR Height is at discretion of designer. The width must be below 780 px.

Fonts to be used: Web 2.0 fonts needed. Must drive message clearly.

*** Long term association oppurtunity exists for the right creative designers for direct work

Business owners

Work

• Cartoonish or cheap graphics

```html
<!DOCTYPE html>
<html lang="en">
<head>
<meta charset="utf-8">
<title>Design Services Flyer</title>
<link rel="stylesheet" href="https://fonts.googleapis.com/css2?family=Arimo:wght@400;700&display=swap">
<style>
  :root {
    --paper-light: #d9cbb6;
    --paper-mid: #b8a58a;
    --paper-dark: #6e5d4a;
    --brown-deep: #3a2314;
    --brown-mid: #6d4f3b;
    --brown-soft: #9b8270;
    --white: #ffffff;
    --grey-band: #9c9c9c;
    --ink: #1e1612;
    --footer: #231f20;
  }
  * { margin: 0; padding: 0; box-sizing: border-box; }
  html, body { width: 1200px; height: 1000px; overflow: hidden; }
  body { font-family: "Arimo", Arial, sans-serif; background: var(--paper-light); }
  .flyer { position: relative; width: 1200px; height: 1000px; overflow: hidden; }
  .backdrop {
    position: absolute; inset: 0;
    background:
      radial-gradient(ellipse 420px 380px at 820px 330px, rgba(40,30,22,.85), rgba(40,30,22,0) 70%),
      radial-gradient(ellipse 300px 240px at 180px 860px, rgba(60,45,32,.7), rgba(60,45,32,0) 70%),
      radial-gradient(ellipse 500px 400px at 300px 300px, #cdbb9f, rgba(205,187,159,0) 70%),
      linear-gradient(135deg, var(--paper-light), var(--paper-mid) 55%, var(--paper-dark));
  }
  .headline { position: absolute; left: 0; width: 1275px; text-align: center; color: var(--white); font-weight: 700; }
  .headline--kicker { top: 6px; font-size: 22px; letter-spacing: 3.6px; }
  .headline--main { top: 34px; font-size: 40px; letter-spacing: 1px; }
  .categories-note { position: absolute; left: 60px; top: 95px; font-size: 19px; font-weight: 700; color: var(--white); letter-spacing: -1.1px; }

  .service-box { position: absolute; left: 60px; width: 365px; }
  .box-head {
    height: 28px; font-weight: 400; font-size: 21px; letter-spacing: 1.8px; color: var(--ink);
    background: linear-gradient(90deg, var(--white) 55%, var(--grey-band) 85%, var(--white));
    padding-left: 73px; line-height: 28px; white-space: nowrap;
  }
  .box-body {
    background: linear-gradient(90deg, var(--brown-deep) 0%, var(--brown-mid) 30%, var(--white) 62%, var(--white) 100%);
    color: var(--ink);
  }
  .box-body ul { list-style: none; }
  .box-body li { white-space: nowrap; }
  .box-body li::before { content: "•"; }

  .corporate { top: 119px; }
  .corporate .box-body { height: 147px; font-size: 14.5px; letter-spacing: 1.8px; padding: 21px 0 0 28px; }
  .corporate .box-body li { line-height: 14.3px; }
  .corporate .box-body li::before { margin-right: 14px; }

  .print { top: 292px; }
  .print .box-head { padding-left: 47px; }
  .print .box-body { height: 148px; display: flex; padding: 10px 0 0 24px; font-size: 12.5px; letter-spacing: .8px;
    background: linear-gradient(90deg, var(--brown-deep) 0%, var(--brown-mid) 25%, var(--white) 45%, var(--white) 80%, var(--brown-mid) 100%); }
  .print .box-body ul:first-child { width: 152px; }
  .print .box-body li { line-height: 13.1px; }
  .print .box-body li::before { margin-right: 11px; }

  .web { top: 468px; height: 170px; }
  .web .box-head { height: 28px; padding-left: 113px;
    background: linear-gradient(90deg, var(--white) 55%, var(--brown-mid) 75%, var(--brown-deep)); }
  .web .box-body { height: 142px; display: flex; padding: 6px 0 0 30px; font-size: 11.8px; letter-spacing: .2px;
    background: linear-gradient(90deg, var(--white) 50%, var(--brown-mid) 75%, var(--brown-deep)); }
  .web .box-body ul:first-child { width: 168px; }
  .web .box-body li { line-height: 14.8px; }
  .web .box-body li::before { margin-right: 12px; }
  .web .col-social { color: #3a2a20; padding-top: 4px; }

  .benefits { position: absolute; left: 60px; top: 647px; width: 450px; }
  .benefits .box-head { height: 52px; line-height: 21px; padding: 6px 0 0 48px; font-size: 18px; letter-spacing: 1.2px; }
  .benefits .box-head span { display: block; padding-left: 44px; }
  .benefits .box-body { height: 143px; padding: 12px 0 0 44px; font-size: 15px; letter-spacing: 1.2px;
    background: linear-gradient(90deg, var(--brown-deep) 0%, var(--brown-mid) 25%, var(--white) 55%, var(--white) 100%); }
  .benefits .box-body li { line-height: 17px; }
  .benefits .box-body li::before { margin-right: 14px; }
  .benefits .wrap-line { padding-left: 26px; }

  .process { position: absolute; left: 545px; top: 628px; width: 603px; }
  .process .box-head { height: 37px; line-height: 32px; padding-left: 38px; font-size: 21px;
    background: linear-gradient(90deg, var(--white) 60%, var(--grey-band) 85%, var(--white)); }
  .process .box-body { height: 178px; padding: 1px 0 0 28px; font-size: 13.5px; letter-spacing: 2.4px;
    background: linear-gradient(90deg, var(--white) 55%, var(--brown-mid) 80%, var(--brown-deep)); }
  .process .box-body li { line-height: 25.6px; }
  .process .box-body li::before { content: none; }

  .portfolio { position: absolute; left: 507px; top: 113px; width: 650px; height: 332px; background: linear-gradient(90deg, #1c1c1c, #4a4a4a 50%, #1f1f1f); }
  .portfolio .shot { position: absolute; }
  .portfolio .label { position: absolute; font-size: 9px; font-weight: 700; color: var(--white); }

  .logo-strip { position: absolute; left: 505px; top: 483px; width: 640px; height: 125px;
    background: linear-gradient(90deg, var(--brown-mid), var(--brown-soft) 30%, #eeeeee 45%, var(--brown-soft) 60%, var(--brown-mid)); }
  .brand { position: absolute; display: flex; align-items: center; gap: 8px; font-weight: 700; white-space: nowrap; }
  .mark { display: inline-block; }

  .footer { position: absolute; left: 60px; top: 843px; width: 1087px; height: 130px;
    background: linear-gradient(90deg, #000 0 160px, var(--brown-mid) 160px, var(--footer) 45%, var(--footer)); }
  .seal { position: absolute; left: 13px; top: 13px; width: 138px; height: 110px; }
  .call { position: absolute; left: 173px; top: 6px; font-size: 19px; font-weight: 700; letter-spacing: 2px; color: var(--white); }
  .contact { position: absolute; display: flex; align-items: center; gap: 14px; color: var(--white); font-size: 16px; letter-spacing: .5px; white-space: nowrap; }
  .contact .svc { font-weight: 700; font-size: 16px; }
  .site-logo { position: absolute; left: 873px; top: 23px; width: 185px; height: 50px; border: 1px solid var(--white);
    color: var(--white); font-size: 19px; padding: 9px 0 0 22px; }
  .site-url { position: absolute; left: 877px; top: 100px; color: var(--white); font-size: 15px; letter-spacing: .5px; white-space: nowrap; }
</style>
</head>
<body>
<div class="flyer">
  <div class="backdrop" role="img" aria-label="Textured aged paper background with dark ink splashes"></div>

  <div class="headline headline--kicker">100% customs graphic designs at the</div>
  <div class="headline headline--main">Most affordable prices</div>
  <div class="categories-note">Our services are available in 36 design categories</div>

  <section class="service-box corporate">
    <h2 class="box-head">Corporate identity</h2>
    <div class="box-body">
      <ul>
        <li>Logo design</li><li>Stationery design</li><li>Business card design</li><li>Envelope design</li>
        <li>Letterhead design</li><li>Presentation folder design</li><li>Slide deck template design</li>
      </ul>
    </div>
  </section>

  <section class="service-box print">
    <h2 class="box-head">Graphics/Print design</h2>
    <div class="box-body">
      <ul>
        <li>T-shirt design</li><li>Brochure design</li><li>Poster design</li><li>Postcard design</li><li>Flyer design</li>
        <li>Book cover design</li><li>Label/ sticker design</li><li>CD cover design</li><li>Trade show display</li>
      </ul>
      <ul>
        <li>Signage design</li><li>Newspaper ad design</li><li>Greeting card/</li><li>Invitation design</li>
        <li>Packaging design</li><li>Vehicle wrap design</li><li>Shopping bag design</li><li>Door hanger design</li><li>Certificate design</li>
      </ul>
    </div>
  </section>

  <section class="service-box web">
    <h2 class="box-head">Web design</h2>
    <div class="box-body">
      <ul>
        <li>Landing page design</li><li>Web page design</li><li>Ecommerce web design</li><li>Blog design</li>
        <li>CMS website design</li><li>Newsletter design</li>
      </ul>
      <ul class="col-social">
        <li>Banner ad design</li><li>Social page design</li><li>Microblog page design</li><li>Video channel design</li><li>Profile page design</li>
      </ul>
    </div>
  </section>

  <section class="benefits">
    <h2 class="box-head">Benefits you get by dealing with<span>Brightmarkstudio.com</span></h2>
    <div class="box-body">
      <ul>
        <li>Creatively crafted functional designs</li>
        <li>Multiple variations of designs submitted</li>
        <li>Variations open to revisions</li>
        <li>Guaranteed 48 hours delivery</li>
        <li>30000+ ready designs also available, all</li>
      </ul>
      <div class="wrap-line">open for 100% Customization at no extra cost</div>
    </div>
  </section>

  <section class="process">
    <h2 class="box-head">Our design process</h2>
    <div class="box-body">
      <ul>
        <li>Careful analysis of your individual &amp; business needs</li>
        <li>Creation of rough hand drawn sketches</li>
        <li>Analyzing sketches and shortlisting them</li>
        <li>Conversion of shortlisted hand drawn sketches to digital formats</li>
        <li>Submission of multiple variations of designs to choose from</li>
        <li>Feedback/suggestions rounds to give final shape to your design</li>
        <li>Delivery of your design in multiple digital formats</li>
      </ul>
    </div>
  </section>

  <section class="portfolio">
    <div class="shot" style="left:19px;top:7px;width:290px;height:148px;background:linear-gradient(90deg,#a49a8c,#6b7d3a 50%,#8bb63a);" role="img" aria-label="Outside spread of a grooming spa brochure with pet photo and spa stones"></div>
    <div class="label" style="left:332px;top:14px;">&lt; &nbsp;OUTSIDE OF BROCHURE</div>
    <div class="shot" style="left:40px;top:170px;width:150px;height:150px;background:linear-gradient(160deg,#7d8a4a,#8dbb35 55%,#4d3a26);" role="img" aria-label="Folded brochure cover mockups with green leaf and stones"></div>
    <div class="label" style="left:534px;top:151px;">INSIDE OF BROCHURE</div>
    <div class="shot" style="left:320px;top:165px;width:310px;height:158px;background:linear-gradient(90deg,#eeeeee,#cfcfcf 40%,#3a3a3a 70%,#111);" role="img" aria-label="Inside spread of a grooming spa brochure with text columns and pet photos"></div>
  </section>

  <section class="logo-strip">
    <div class="brand" style="left:16px;top:44px;font-size:22px;color:#f0a030;"><span class="mark" style="width:16px;height:16px;border-radius:50%;background:#f0a030;"></span>Crewline Staffing</div>
    <div class="brand" style="left:250px;top:52px;font-size:14px;color:#2a1a10;"><span class="mark" style="width:12px;height:12px;border-radius:50%;background:#e3b21c;"></span>Keystone Masonry</div>
    <div style="position:absolute;left:210px;top:80px;width:205px;height:21px;background:#111;"></div>
    <div class="brand" style="left:262px;top:83px;font-size:11px;color:#e3b21c;">Keystone Masonry</div>
    <div class="brand" style="left:445px;top:30px;font-size:14px;color:#4a7a22;"><span class="mark" style="width:12px;height:12px;background:#e86a2a;"></span>Urban Voltica</div>
    <div style="position:absolute;left:425px;top:66px;width:195px;height:39px;background:#111;"></div>
    <div class="brand" style="left:445px;top:78px;font-size:14px;color:#8cc63e;"><span class="mark" style="width:12px;height:12px;background:#e86a2a;"></span>Urban Voltica</div>
  </section>

  <footer class="footer">
    <svg class="seal" viewBox="0 0 138 110" role="img" aria-label="Satisfaction guarantee seal">
      <circle cx="69" cy="55" r="52" fill="none" stroke="#bbbbbb" stroke-width="5"/>
      <circle cx="69" cy="55" r="40" fill="none" stroke="#bbbbbb" stroke-width="2"/>
    </svg>
    <div class="call">call us now: +11 55501 23456</div>
    <div class="contact" style="left:175px;top:40px;"><span class="svc">Pingo</span><span style="margin-left:58px">xxxxxxxxxxxxxxxxxx</span></div>
    <div class="contact" style="left:460px;top:42px;"><span class="svc" style="color:#4aa3df">Netline</span><span style="margin-left:20px">xxxxxxxxxxxx</span></div>
    <div class="contact" style="left:175px;top:97px;"><span class="svc">Talkwave</span><span style="margin-left:8px">xxxxxxxxxxxxxxxxx</span></div>
    <div class="contact" style="left:480px;top:92px;"><span class="mark" style="width:14px;height:14px;border-radius:50%;background:#2aa5e0;"></span><span class="svc">Callbox</span><span style="margin-left:18px">xxxxxxxxxxxxx</span></div>
    <div class="site-logo">site logo</div>
    <div class="site-url">www.brightmarkstudio.com</div>
  </footer>
</div>
</body>
</html>
```